Modern Label Design for Fruity Drink (300ml PET)

Dear Graphic Designers,

JOB BRIEF
We are a beverage manufacturer in South Africa seeking a creative wrap-around label design for our exciting new fruity drink range called Zindelu. Although our beverage doesn't contain real fruit, it's crafted to emulate the taste and appearance of authentic fruit juices, complete with essential benefits like vitamins and minerals that are contained in real fruit. Despite being priced competitively, we want the design to exude a premium feel likened to luxury juices and drinks.

TARGET MARKET
The design must possess a modern appeal that resonates with both children and adults.

DESIGN GUIDELINES
- Modern and Elegant
- Colourful
- Evokes a sense of fruit without direct explicit fruit depictions

MANDATORY ELEMENTS
1. Flavoured Drink: Law states that "Flavoured Drink" needs to be written on the front of the label, potentially integrated with the flavor name, e.g., "Orange Flavoured Drink."
2. No Fruit Images: Avoid using real fruit images, opting instead for textures and shapes that very slightly allude to the essence of fruit flavour. This is also a legal constraint.
3. Toucan Mascot: Consider incorporating a toucan or parrot as a potential mascot.
4. Logo: We have a logo, you may use this and adapt it, or design your own.
5. Claims: We need a claim on the front "High in Vitamin C, B and Zinc"

DESIGN INSPIRATION AND WARNING
Avoid drawing inspiration from our initial design attempt, shared in the files section. This design is deemed unsuitable as it appears too busy, has an 'old school' vibe, and may be perceived as exclusively for children. We aspire for a premium design that caters to adults while still being colourful.

FLAVORS
"Golden Swirl" or alternatively "Orange Flavoured Drink"
"Velvet Pop" or alternatively "Berry Flavoured Drink"
"Island Drift" or alternatively "Tropical Flavoured Drink"
"Crisp Meadow" or alternatively "Apple Flavoured Drink"

We encourage your innovative designs. Thank you for your participation, and we look forward to witnessing your creative brilliance!

Best regards,
The Marketing Team

Target Market(s)

Adults and Children (Premium)

Industry/Entity Type

Beverages

Colors

Designer to choose colors to be used in the design.

Requirements
Must have
• Premium and Colourful
Nice to have
• It would be nice to have a new or updated logo (but we have existing logo if needed), and it would be nice to have a parrot or toucan mascot somewhere
Should not have
• Looking too much like a children's fruity drink. Shouldn't contain real images or illustrations of fruit (only vaguely resembling the fruit through shapes and textures)

```html
<!DOCTYPE html>
<html lang="en">
<head>
<meta charset="utf-8">
<title>Zindelu — Flavoured Drink Labels</title>
<link rel="stylesheet" href="https://fonts.googleapis.com/css2?family=Rubik:wght@900&family=Montserrat:wght@500;700&display=swap">
<style>
  :root {
    --backdrop: #bcbcbc;
    --label-base: #ececec;
    --brand-blue: #2b4aa6;
    --mascot-blue: #5aa3cf;
    --golden-blob: #d4ae3c;
    --golden-ink: #d0512a;
    --velvet-blob: #8f47db;
    --velvet-ink: #5a22a8;
    --island-blob: #c9663f;
    --island-ink: #c8452c;
    --meadow-blob: #c93639;
    --meadow-ink: #bf252a;
  }
  * { box-sizing: border-box; margin: 0; padding: 0; }
  html, body { width: 1200px; height: 821px; overflow: hidden; }
  body {
    background: var(--backdrop);
    display: flex;
    align-items: center;
    justify-content: center;
    gap: 30px;
    font-family: "Montserrat", sans-serif;
  }
  .label {
    position: relative;
    width: 260px;
    height: 272px;
    background: var(--label-base);
    overflow: hidden;
    color: var(--blob);
  }
  .label--golden { --blob: var(--golden-blob); --ink: var(--golden-ink); }
  .label--velvet { --blob: var(--velvet-blob); --ink: var(--velvet-ink); }
  .label--island { --blob: var(--island-blob); --ink: var(--island-ink); }
  .label--meadow { --blob: var(--meadow-blob); --ink: var(--meadow-ink); }
  .label__blobs { position: absolute; inset: 0; width: 100%; height: 100%; }
  .brand {
    position: absolute;
    top: 34px;
    left: 0;
    right: 0;
    text-align: center;
    font-family: "Rubik", sans-serif;
    font-weight: 900;
    font-size: 50px;
    line-height: 1;
    color: var(--brand-blue);
    display: flex;
    align-items: center;
    justify-content: center;
    gap: 8px;
  }
  .brand__dot {
    width: 14px; height: 14px; border-radius: 50%;
    background: var(--brand-blue);
  }
  .mascot {
    position: absolute;
    left: 28px;
    top: 94px;
    width: 52px;
    height: 56px;
    border-radius: 26px 26px 10px 10px;
    background: linear-gradient(160deg, var(--mascot-blue), #d9ac3a);
  }
  .flavour {
    position: absolute;
    top: 160px;
    left: 0; right: 0;
    text-align: center;
    color: var(--ink);
  }
  .flavour__name {
    font-family: "Rubik", sans-serif;
    font-weight: 900;
    font-size: 21px;
    line-height: 0.95;
    text-transform: uppercase;
  }
  .flavour__descriptor {
    margin-top: 4px;
    font-size: 5.5px;
    font-weight: 500;
    letter-spacing: 0.3px;
    text-transform: uppercase;
  }
  .claim {
    position: absolute;
    top: 220px;
    left: 50%;
    transform: translateX(-50%);
    background: var(--ink);
    color: #fff;
    border-radius: 3px;
    padding: 2px 6px;
    text-align: center;
    font-size: 7px;
    line-height: 1.05;
    text-transform: uppercase;
    white-space: nowrap;
  }
  .claim strong { font-family: "Rubik", sans-serif; font-weight: 900; display: block; }
  .volume {
    position: absolute;
    top: 250px;
    left: 0; right: 0;
    text-align: center;
    font-size: 7px;
    font-weight: 700;
    color: var(--ink);
  }
</style>
</head>
<body>

<svg width="0" height="0" style="position:absolute" aria-hidden="true">
  <defs>
    <g id="label-blobs" fill="currentColor">
      <path d="M0 0H60C72 22 38 42 50 72C60 100 22 112 0 118Z"/>
      <path d="M185 0H260V104C232 112 212 84 228 62C244 40 198 30 185 0Z"/>
      <path d="M260 138V212C238 218 218 196 228 176C238 158 232 144 260 138Z"/>
      <path d="M0 168C30 152 62 172 56 202C50 232 20 242 0 248Z"/>
      <path d="M176 272C168 240 190 214 226 218C250 221 260 238 260 250V272Z"/>
      <path d="M68 272C80 254 110 254 118 272Z"/>
    </g>
  </defs>
</svg>

<article class="label label--golden">
  <svg class="label__blobs" viewBox="0 0 260 272" aria-hidden="true"><use href="#label-blobs"/></svg>
  <div class="brand"><span class="brand__dot"></span>Zindelu</div>
  <div class="mascot" role="img" aria-label="Parrot mascot illustration"></div>
  <div class="flavour">
    <h2 class="flavour__name">Golden<br>Swirl</h2>
    <p class="flavour__descriptor">Orange flavoured drink</p>
  </div>
  <div class="claim">High in vitamin<strong>C, B and zinc</strong></div>
  <p class="volume">330 ml</p>
</article>

<article class="label label--velvet">
  <svg class="label__blobs" viewBox="0 0 260 272" aria-hidden="true"><use href="#label-blobs"/></svg>
  <div class="brand"><span class="brand__dot"></span>Zindelu</div>
  <div class="mascot" role="img" aria-label="Parrot mascot illustration"></div>
  <div class="flavour">
    <h2 class="flavour__name">Velvet<br>Pop</h2>
    <p class="flavour__descriptor">Berry flavoured drink</p>
  </div>
  <div class="claim">High in vitamin<strong>C, B and zinc</strong></div>
  <p class="volume">330 ml</p>
</article>

<article class="label label--island">
  <svg class="label__blobs" viewBox="0 0 260 272" aria-hidden="true"><use href="#label-blobs"/></svg>
  <div class="brand"><span class="brand__dot"></span>Zindelu</div>
  <div class="mascot" role="img" aria-label="Parrot mascot illustration"></div>
  <div class="flavour">
    <h2 class="flavour__name">Island<br>Drift</h2>
    <p class="flavour__descriptor">Tropical flavoured drink</p>
  </div>
  <div class="claim">High in vitamin<strong>C, B and zinc</strong></div>
  <p class="volume">330 ml</p>
</article>

<article class="label label--meadow">
  <svg class="label__blobs" viewBox="0 0 260 272" aria-hidden="true"><use href="#label-blobs"/></svg>
  <div class="brand"><span class="brand__dot"></span>Zindelu</div>
  <div class="mascot" role="img" aria-label="Parrot mascot illustration"></div>
  <div class="flavour">
    <h2 class="flavour__name">Crisp<br>Meadow</h2>
    <p class="flavour__descriptor">Apple flavoured drink</p>
  </div>
  <div class="claim">High in vitamin<strong>C, B and zinc</strong></div>
  <p class="volume">330 ml</p>
</article>

</body>
</html>
```